Packaging for Hair Fibers Product

We are a start up company looking for a new packaging design for hair building fibers. These are aimed at predominantly men but also women as well. We already have a logo and i have the packaging design from our competitors. We are wanting to keep the look masculine as 90% of our users will be middle aged men. We would like the colours to be black and white but are open to other colours as well.
It will need to have our logo and the following somewhere on the front.
"Instant Fuller & Thicker Hair" & "Natural Hair Building Fibers" "28g" or "Net Weight 28g"
We only need the front of the packaging designed, please make the other sides of the packaging the same colour but blank.
Target Market(s)
Men 25+
Industry/Entity Type
Hair And Beauty
Requirements
Must have
- Logo which i have included. and the following somewhere on the front.
- "Instant Fuller & Thicker Hair" ; "Natural Hair Building Fibers" "28g" or "Net Weight 28g"
Nice to have
- Make it stand out from the competition or similar to the brantiq example.

```html
<!DOCTYPE html>
<html lang="en">
<head>
<meta charset="utf-8">
<title>Fortivo – Natural Hair Building Fibers Packaging</title>
<link rel="stylesheet" href="https://fonts.googleapis.com/css2?family=Montserrat:wght@300;400&family=Oswald:wght@500;600&display=swap">
<style>
  :root {
    --page-bg: #ffffff;
    --box-black: #121212;
    --box-black-deep: #0a0a0a;
    --box-sheen: #2a2a2a;
    --side-black: #0d0d0d;
    --ink-white: #f2f2f2;
    --ink-soft: #c9c9c9;
    --ink-muted: #9a9a9a;
  }
  * { margin: 0; padding: 0; box-sizing: border-box; }
  html, body {
    width: 1200px;
    height: 738px;
    overflow: hidden;
    background: var(--page-bg);
  }
  .canvas {
    position: relative;
    width: 1200px;
    height: 738px;
    display: flex;
    align-items: center;
    justify-content: center;
  }
  .dieline {
    display: flex;
    height: 640px;
  }
  .panel {
    position: relative;
    height: 100%;
  }
  .panel--side {
    width: 180px;
    background: linear-gradient(180deg, var(--side-black), var(--box-black-deep));
    border-right: 1px solid #1f1f1f;
    padding: 0 18px;
  }
  .panel--front {
    width: 300px;
    background:
      radial-gradient(ellipse 120% 70% at 70% 35%, var(--box-sheen) 0%, var(--box-black) 55%, var(--box-black-deep) 100%);
    text-align: center;
    color: var(--ink-white);
  }
  .side-brand {
    position: absolute;
    top: 400px;
    left: 18px;
    font-family: "Montserrat", sans-serif;
    font-weight: 300;
    font-size: 11px;
    letter-spacing: 2px;
    color: var(--ink-white);
  }
  .side-copy {
    position: absolute;
    top: 440px;
    left: 18px;
    right: 18px;
    font-family: "Montserrat", sans-serif;
    font-weight: 400;
    font-size: 6.5px;
    line-height: 1.55;
    color: var(--ink-soft);
    text-align: justify;
  }
  .brand {
    position: absolute;
    top: 96px;
    left: 0;
    right: 0;
    font-family: "Montserrat", sans-serif;
    font-weight: 300;
    font-size: 30px;
    letter-spacing: 5px;
    color: var(--ink-white);
  }
  .tagline {
    position: absolute;
    top: 296px;
    left: 0;
    right: 0;
    font-family: "Montserrat", sans-serif;
    font-weight: 400;
    font-size: 10.5px;
    color: var(--ink-soft);
  }
  .rule {
    position: absolute;
    top: 322px;
    left: 60px;
    right: 60px;
    height: 1px;
    background: var(--ink-soft);
  }
  .product-name {
    position: absolute;
    top: 340px;
    left: 0;
    right: 0;
    font-family: "Oswald", sans-serif;
    text-transform: uppercase;
    line-height: 1;
    color: var(--ink-white);
  }
  .product-name__line1 {
    display: block;
    font-weight: 600;
    font-size: 27px;
    letter-spacing: 0.5px;
  }
  .product-name__line2 {
    display: block;
    margin-top: 6px;
    font-weight: 600;
    font-size: 44px;
    letter-spacing: 1px;
  }
  .product-name__line3 {
    display: block;
    margin-top: 6px;
    font-weight: 500;
    font-size: 40px;
    letter-spacing: 9px;
    padding-left: 9px;
  }
  .net-weight {
    position: absolute;
    bottom: 30px;
    left: 0;
    right: 0;
    font-family: "Montserrat", sans-serif;
    font-weight: 400;
    font-size: 12px;
    color: var(--ink-soft);
  }
</style>
</head>
<body>
  <main class="canvas">
    <div class="dieline">
      <section class="panel panel--side" aria-label="Side panel">
        <div class="side-brand">FORTIVO</div>
        <p class="side-copy">Sprinkle the fibers over thinning areas of dry hair, then gently pat to help them bond with your own strands. Finish with a light mist of hair spray to lock the look in place. Results last until your next wash. For external use only. Keep away from eyes and store in a cool dry place.</p>
      </section>
      <section class="panel panel--front" aria-label="Front panel">
        <div class="brand">FORTIVO</div>
        <p class="tagline">Instant Fuller &amp; Thicker Hair</p>
        <div class="rule"></div>
        <h1 class="product-name">
          <span class="product-name__line1">Natural Hair</span>
          <span class="product-name__line2">Building</span>
          <span class="product-name__line3">Fibers</span>
        </h1>
        <p class="net-weight">Net Weight 28g</p>
      </section>
    </div>
  </main>
</body>
</html>
```